SHG business cards

design a business card

(Generators . Lighting Towers . De-watering Pumps . Compressors) put under the logo please. my details are Marek Oyelaran (Director) 0461527308 silverpinehaulgroup@postvane.com

```html
<!DOCTYPE html>
<html lang="en">
<head>
<meta charset="UTF-8">
<title>SHG business cards</title>
<link rel="stylesheet" href="https://fonts.googleapis.com/css2?family=Michroma&family=Open+Sans:wght@400&display=swap">
<style>
  :root {
    --backdrop: #2b2b2b;
    --card: #050505;
    --gold: #d9963a;
    --silver: #b9b9bb;
    --white: #f2f2f2;
    --rule: #8a8a8a;
  }
  * { margin: 0; padding: 0; box-sizing: border-box; }
  html, body { width: 1200px; height: 694px; overflow: hidden; background: var(--backdrop); }
  .stage {
    position: relative; width: 1200px; height: 694px;
    display: flex; align-items: center; justify-content: center; gap: 60px;
  }
  .card {
    position: relative; width: 520px; height: 300px;
    background: var(--card); border-radius: 20px;
    box-shadow: 0 12px 30px rgba(0,0,0,.45);
    font-family: "Open Sans", sans-serif; color: var(--white);
  }
  .brand { display: flex; align-items: center; gap: 10px; }
  .brand-square { width: 16px; height: 16px; background: var(--gold); flex: none; }
  .brand-name {
    font-family: "Michroma", sans-serif; color: var(--gold);
    text-transform: uppercase; line-height: 1.25;
  }
  .services {
    font-family: "Michroma", sans-serif; text-transform: uppercase;
    color: var(--white); line-height: 1.3;
  }
  /* front */
  .card-front { display: flex; flex-direction: column; align-items: center; justify-content: center; gap: 22px; }
  .card-front .brand-name { font-size: 24px; }
  .card-front .brand-square { width: 22px; height: 22px; }
  .card-front .services { font-size: 17px; text-align: left; }
  /* back */
  .card-back .brand { position: absolute; top: 34px; right: 30px; gap: 7px; }
  .card-back .brand-name { font-size: 12px; }
  .card-back .brand-square { width: 11px; height: 11px; }
  .card-back .services { position: absolute; top: 64px; right: 30px; font-size: 8.5px; }
  .holder { position: absolute; left: 34px; bottom: 72px; }
  .holder-name { font-family: "Michroma", sans-serif; color: var(--gold); font-size: 19px; text-transform: uppercase; }
  .holder-role { font-size: 12px; margin-top: 4px; }
  .divider { position: absolute; left: 34px; right: 30px; bottom: 58px; height: 1px; background: var(--rule); }
  .contact { position: absolute; bottom: 28px; display: flex; align-items: center; gap: 8px; font-size: 13px; }
  .contact-phone { left: 34px; }
  .contact-email { right: 30px; }
  .contact svg { width: 14px; height: 14px; fill: var(--gold); }
</style>
</head>
<body>
<main class="stage">
  <section class="card card-front">
    <div class="brand">
      <span class="brand-square"></span>
      <span class="brand-name">Silver Pine<br>Haul Group</span>
    </div>
    <p class="services">(Generators, Lighting<br>Towers, De-watering<br>Pumps, Compressors)</p>
  </section>

  <section class="card card-back">
    <div class="brand">
      <span class="brand-square"></span>
      <span class="brand-name">Silver Pine Haul Group</span>
    </div>
    <p class="services">(Generators, Lighting<br>Towers, De-watering<br>Pumps, Compressors)</p>

    <div class="holder">
      <p class="holder-name">Marek Oyelaran</p>
      <p class="holder-role">Director</p>
    </div>
    <div class="divider"></div>
    <p class="contact contact-phone">
      <svg viewBox="0 0 24 24" aria-hidden="true"><path d="M6.6 10.8a15.1 15.1 0 0 0 6.6 6.6l2.2-2.2a1 1 0 0 1 1-.25 11.4 11.4 0 0 0 3.6.57 1 1 0 0 1 1 1V20a1 1 0 0 1-1 1A17 17 0 0 1 3 4a1 1 0 0 1 1-1h3.5a1 1 0 0 1 1 1c0 1.25.2 2.45.57 3.57a1 1 0 0 1-.25 1z"/></svg>
      0461527308
    </p>
    <p class="contact contact-email">
      <svg viewBox="0 0 24 24" aria-hidden="true"><path d="M2 5h20v14H2z M4 7v.5l8 5 8-5V7z" fill-rule="evenodd"/></svg>
      silverpinehaulgroup@postvane.com
    </p>
  </section>
</main>
</body>
</html>
```